LearnNest Business Cards

I will be teaching Zorvo and Kelvix classes to the 55+community.Small groups of 10(max), or individual lessons.Beginner and Advance ClassesTraining Material ProvidedThis is a new business in Florida.I hope to order business cards and brochures.I found sample of business card on Printobel - see below. I like the looks of this card, instead of a lighthouseI would like an apple with the red and white stripes. The red and white apple will be my logo. Thank you,Marla Quenby
Target Market(s)
55+ Adults
Industry/Entity Type
Business
Contact Information for Business Card
Marla ApplebyOwner/Instructor772 571-7011iteachdiane@gmail.com
Look and feel
Each slider illustrates characteristics of the customer's brand and the style your logo design should communicate.

```html
<!DOCTYPE html>
<html lang="en">
<head>
<meta charset="utf-8">
<title>LearnNest Business Card</title>
<link rel="stylesheet" href="https://fonts.googleapis.com/css2?family=Lato:wght@400;700&display=swap">
<style>
  :root {
    --backdrop: #3a3431;
    --card: #1c1c1d;
    --card-edge: #2a2a2b;
    --green: #3fa447;
    --red: #b3252a;
    --silver: #a9a9ab;
    --divider: #3a3a3b;
  }
  * { margin: 0; padding: 0; box-sizing: border-box; }
  html, body { width: 1200px; height: 844px; overflow: hidden; }
  body {
    background: var(--backdrop);
    font-family: "Lato", sans-serif;
    position: relative;
  }
  .card {
    position: absolute;
    top: 274px;
    width: 520px;
    height: 297px;
    background: var(--card);
    border: 1px solid var(--card-edge);
    border-radius: 3px;
    box-shadow: 0 10px 28px rgba(0,0,0,.45);
  }
  .card--front { left: 50px; }
  .card--back { left: 630px; display: flex; align-items: center; justify-content: center; }

  .brand {
    position: absolute;
    left: 34px;
    top: 132px;
    display: flex;
    align-items: center;
    gap: 8px;
  }
  .brand__dot { width: 16px; height: 16px; border-radius: 50%; background: var(--green); }
  .brand__name { color: var(--red); font-weight: 700; font-size: 28px; letter-spacing: .2px; }

  .divider {
    position: absolute;
    left: 246px;
    top: 58px;
    width: 1px;
    height: 180px;
    background: var(--divider);
  }
  .details { position: absolute; left: 264px; top: 60px; color: var(--green); }
  .details__name { font-size: 24px; font-weight: 400; line-height: 1.1; }
  .details__title { color: var(--red); font-size: 14px; margin-bottom: 16px; }
  .details__address { font-size: 15px; line-height: 1.3; margin-bottom: 16px; }
  .details__contact { list-style: none; font-size: 15px; line-height: 1.35; }
  .details__label { color: var(--red); }

  .back-brand { color: var(--silver); font-weight: 700; font-size: 40px; letter-spacing: .5px; }
</style>
</head>
<body>
  <section class="card card--front">
    <div class="brand">
      <span class="brand__dot"></span>
      <span class="brand__name">LearnNest</span>
    </div>
    <div class="divider"></div>
    <div class="details">
      <p class="details__name">Dorin Vascal</p>
      <p class="details__title">Managing Director</p>
      <p class="details__address">12345, Address Goes Here<br>Country Name, 123456.</p>
      <ul class="details__contact">
        <li><span class="details__label">T:</span> 044-418 390 226</li>
        <li><span class="details__label">E:</span> info@learnnest.org</li>
        <li><span class="details__label">W:</span>www.learnnestclass.org</li>
      </ul>
    </div>
  </section>

  <section class="card card--back">
    <span class="back-brand">LearnNest</span>
  </section>
</body>
</html>
```